Criminal Defense Firm looking for an edge in business card design

Established Criminal Defense Firm looking to refresh business card. We already have logo and website, but our business cards are extremely boring. We would like to also have something on the backside of card.
Needs to be business oriented, but creative.
We provide services to professionals such as doctors, lawyers, politicians, etc.
Our specialty is to protect professional licenses when facing a criminal matter.

Update on March 10, 2015: This project is for a Business Card Design. The winner in this project will be assigned the next (1on1) project which incidentally is also entitled Business Card Design. I'm sorry for this confusion. The 1on1 project will not be for Business Card Design but will be for Stationery-Envelope Design. Thank you for your attention and continued participation.

Target Market(s)

People accused of a crime

Industry/Entity Type

Business

Contact Information for Business Card

Simple, strong, professional

Colors
85abd2
3176b5
0355a3

```html
<!DOCTYPE html>
<html lang="en">
<head>
<meta charset="utf-8">
<title>Calloway Brennan Law Corporation — Business Cards</title>
<link rel="stylesheet" href="https://fonts.googleapis.com/css2?family=Arimo:wght@400&display=swap">
<style>
  :root {
    --backdrop: #9a9a9a;
    --card-white: #ffffff;
    --brand-blue: #1566b3;
    --mid-blue: #3176b5;
    --light-blue: #85abd2;
    --ink: #1a1a1a;
  }
  html, body {
    margin: 0;
    padding: 0;
    width: 1200px;
    height: 1000px;
    overflow: hidden;
    background: var(--backdrop);
    font-family: "Arimo", Arial, sans-serif;
  }
  .stage {
    position: relative;
    width: 1200px;
    height: 1000px;
  }
  .card {
    position: absolute;
    top: 357px;
    width: 500px;
    height: 286px;
    box-shadow: 0 6px 18px rgba(0,0,0,0.25);
  }
  .card--front {
    left: 70px;
    background: var(--brand-blue);
  }
  .card--back {
    left: 630px;
    background: var(--card-white);
  }
  .front-art {
    position: absolute;
    inset: 0;
  }
  .front-name {
    font-family: "Arimo", Arial, sans-serif;
    font-weight: 400;
    fill: var(--card-white);
    font-size: 14px;
    letter-spacing: 1px;
  }
  .firm-name {
    position: absolute;
    left: 90px;
    top: 34px;
    width: 160px;
    text-align: center;
    color: var(--ink);
    font-size: 12px;
    line-height: 13px;
    letter-spacing: 1.2px;
    text-transform: uppercase;
  }
  .attorney {
    position: absolute;
    left: 40px;
    top: 92px;
    width: 260px;
    text-align: center;
  }
  .attorney-name {
    color: var(--mid-blue);
    font-size: 19px;
    letter-spacing: 1.5px;
    line-height: 22px;
  }
  .attorney-title {
    color: var(--light-blue);
    font-size: 10px;
    letter-spacing: 1.5px;
    line-height: 14px;
  }
  .divider {
    position: absolute;
    left: 35px;
    top: 144px;
    width: 430px;
    height: 4px;
    background: var(--brand-blue);
  }
  .address {
    position: absolute;
    right: 35px;
    top: 94px;
    text-align: right;
    color: var(--mid-blue);
    font-size: 10.5px;
    line-height: 13px;
    letter-spacing: 0.6px;
    text-transform: uppercase;
  }
  .contact {
    position: absolute;
    left: 35px;
    top: 196px;
    color: var(--mid-blue);
    font-size: 10.5px;
    line-height: 13px;
    letter-spacing: 0.6px;
  }
  .contact-email {
    text-transform: uppercase;
    margin-bottom: 2px;
  }
</style>
</head>
<body>
<main class="stage">
  <section class="card card--front" aria-label="Card front">
    <svg class="front-art" width="500" height="286" viewBox="0 0 500 286">
      <line x1="0" y1="143" x2="500" y2="143" stroke="#ffffff" stroke-width="3"/>
      <circle cx="250" cy="143" r="82" fill="var(--brand-blue)" stroke="#ffffff" stroke-width="6"/>
      <text class="front-name" x="250" y="138" text-anchor="middle">CALLOWAY</text>
      <text class="front-name" x="250" y="158" text-anchor="middle">BRENNAN</text>
    </svg>
  </section>

  <section class="card card--back" aria-label="Card back">
    <div class="firm-name">Calloway<br>Brennan<br>Law Corporation</div>
    <div class="attorney">
      <div class="attorney-name">DANIEL CALLOWAY</div>
      <div class="attorney-title">ATTORNEY AT LAW</div>
    </div>
    <div class="address">
      1180 Meridian Avenue<br>
      Suite 210, Riverton<br>
      California 90000
    </div>
    <div class="divider"></div>
    <div class="contact">
      <div class="contact-email">daniel@cbdefenselaw.com</div>
      <div>T: 555-201-4830</div>
      <div>F: 555-201-4831</div>
    </div>
  </section>
</main>
</body>
</html>
```